Corvallin Property Solutions need a business card design

Hello guys. We would need a business card design asap please.
We are a start up property investment business based in London UK specialised in buying, selling, managing and letting properties and helping distressed property owners.
The name of our Business is Corvallin, the logo symbolises the four fundamental elements of the world (earth, air, fire and water) and so it stands for strength, stability, longevity.
We would like the business card to communicate professionalism and reliability. Many many thanks indeed for your work.

Details:

1.) Marisol Dunkley
Property Investor
Mobile: +44(0)7700362517
Email: marisol.corvallin@quilbrook.example

2.) Tomas Brindle
Property Investor
Mobile: +44(0)7700845926
Email: tomas.corvallin@quilbrook.example

Industry/Entity Type

Investment

```html
<!DOCTYPE html>
<html lang="en">
<head>
<meta charset="utf-8">
<title>Corvallin Property Solutions – Business Card</title>
<link rel="stylesheet" href="https://fonts.googleapis.com/css2?family=Lato:wght@400;700;900&display=swap">
<style>
  :root {
    --page-bg: #dcdcdc;
    --card-bg: #ffffff;
    --navy: #1f3c88;
    --red: #d3232b;
    --green: #2f9a45;
    --band-blue: #2551a6;
    --band-red: #d3232b;
    --band-green: #2a9a47;
    --brand-grey: #8e8e8e;
    --ink: #1a1a1a;
    --divider: #555555;
  }
  * { box-sizing: border-box; margin: 0; padding: 0; }
  html, body {
    width: 1200px; height: 926px; overflow: hidden;
    background: var(--page-bg);
    font-family: "Lato", Arial, sans-serif;
  }
  .sheet {
    width: 1200px; height: 926px;
    display: flex; flex-direction: column; align-items: center; justify-content: center;
    gap: 40px;
  }
  .card {
    position: relative;
    width: 640px; height: 400px;
    background: var(--card-bg);
    overflow: hidden;
    box-shadow: 0 6px 18px rgba(0,0,0,0.18);
  }

  /* Front */
  .card--front { display: flex; align-items: center; justify-content: center; }
  .brand-name {
    color: var(--brand-grey);
    font-weight: 900;
    font-size: 40px;
    letter-spacing: 3px;
    text-transform: uppercase;
    text-align: center;
    line-height: 1.15;
  }

  /* Back */
  .card__brand {
    position: absolute; top: 44px; left: 0; right: 0;
    text-align: center;
    color: var(--ink);
    font-weight: 900;
    font-size: 22px;
    letter-spacing: 1.5px;
    text-transform: uppercase;
    line-height: 1.15;
  }
  .contacts {
    position: absolute; top: 132px; left: 0; right: 0;
    display: flex; justify-content: center;
  }
  .person { width: 300px; padding: 0 16px; }
  .person--left { text-align: right; }
  .person--right { text-align: left; padding-top: 26px; }
  .person__divider { width: 1px; height: 92px; background: var(--divider); margin-top: 26px; }
  .person__name {
    color: var(--navy); font-weight: 700; font-size: 21px;
    letter-spacing: 1px; text-transform: uppercase; line-height: 1.1;
  }
  .person__role { color: var(--red); font-weight: 700; font-size: 14px; margin-bottom: 6px; }
  .person__line { color: var(--navy); font-size: 13.5px; line-height: 1.55; white-space: nowrap; }
  .person__label { color: var(--green); font-weight: 700; }

  .card__bands { position: absolute; left: 0; bottom: 0; width: 640px; height: 400px; }
</style>
</head>
<body>
<main class="sheet">

  <section class="card card--front" aria-label="Business card front">
    <p class="brand-name">Corvallin<br>Property Solutions</p>
  </section>

  <section class="card card--back" aria-label="Business card back">
    <p class="card__brand">Corvallin<br>Property Solutions</p>

    <div class="contacts">
      <div class="person person--left">
        <p class="person__name">Tomas Brindle</p>
        <p class="person__role">Property Investor</p>
        <p class="person__line">+44(0)7700845926 : <span class="person__label">M</span></p>
        <p class="person__line">tomas.corvallin@quilbrook.example : <span class="person__label">E</span></p>
      </div>
      <div class="person__divider"></div>
      <div class="person person--right">
        <p class="person__name">Marisol Dunkley</p>
        <p class="person__role">Property Investor</p>
        <p class="person__line"><span class="person__label">M</span> : +44(0)7700362517</p>
        <p class="person__line"><span class="person__label">E</span> : marisol.corvallin@quilbrook.example</p>
      </div>
    </div>

    <svg class="card__bands" viewBox="0 0 640 400" aria-hidden="true">
      <path fill="var(--band-green)" d="M0,238 C140,300 320,332 640,330 L640,400 L0,400 Z"/>
      <path fill="var(--band-red)"   d="M0,296 C160,330 340,342 640,338 L640,400 L0,400 Z"/>
      <path fill="var(--band-blue)"  d="M0,314 C170,340 350,352 640,346 L640,400 L0,400 Z"/>
    </svg>
  </section>

</main>
</body>
</html>
```